Amber Reed Landing Postcard Design

I am a real estate agent
I am marketing a gulf access waterfront community is southwest florida. I would like to do Just Listed and Just Sold post cards

So this will be two different post cards

In addition to the pictures I have uploaded mock ups of an idea of what I would like for the front and the back

I would like this done glossy on both sides

```html
<!DOCTYPE html>
<html lang="en">
<head>
<meta charset="utf-8">
<title>Amber Reed Landing Postcards</title>
<link rel="stylesheet" href="https://fonts.googleapis.com/css2?family=Old+Standard+TT:wght@400;700&family=Jost:wght@500&family=Arimo:wght@400;700&family=Roboto+Condensed:wght@400&display=swap">
<style>
  :root{
    --ink:#000;
    --paper:#fff;
    --text:#1a1a1a;
    --rule:#333;
    --sky:#6f9fd4;
    --sea:#2c5f8c;
    --marsh:#6b7a45;
    --land:#c7c2a5;
    --map-green:#3f9a4a;
  }
  *{margin:0;padding:0;box-sizing:border-box}
  html,body{width:1200px;height:919px;overflow:hidden;background:var(--paper)}
  .sheet{position:absolute;left:0;top:0;width:1100px;height:843px;transform:scale(1.0909);transform-origin:0 0}
  .front{position:absolute;left:7px;width:532px;height:412px;background:var(--ink)}
  .back{position:absolute;left:560px;width:533px;height:411px;background:var(--paper);border:1px solid var(--rule)}
  .card-sold{top:8px}
  .card-listed{top:427px}
  .photo{position:absolute}
  .map-inset{left:12px;top:13px;width:153px;height:122px;background:linear-gradient(135deg,#fff 0%,#fff 20%,var(--map-green) 21%,var(--map-green) 60%,#fff 61%)}
  .aerial{background:linear-gradient(180deg,#9cc0e6 0%,#4d7fb0 30%,#7c8b6a 45%,var(--land) 65%,var(--marsh) 100%)}
  .canal{background:linear-gradient(180deg,#8fb4e6 0%,#b9d1ee 30%,#5a8a4e 45%,#3a6f8f 60%,var(--sea) 100%)}
  .headline{position:absolute;left:0;width:518px;text-align:center;color:var(--paper)}
  .kicker{font-family:"Old Standard TT",serif;font-weight:700;font-size:29px;letter-spacing:2px}
  .place{font-family:"Jost",sans-serif;font-weight:500;font-size:38px;letter-spacing:.5px}
  .badge{position:absolute;width:178px;height:47px;background:var(--ink);border-radius:10px;display:flex;align-items:center;gap:7px;padding-left:8px}
  .badge-mark{width:18px;height:18px;background:var(--paper)}
  .badge-text{font-family:"Roboto Condensed",sans-serif;color:var(--paper);font-size:15px;line-height:19px}
  .sender{position:absolute;left:16px;top:27px;display:flex;gap:10px}
  .sender-mark{width:38px;height:38px;background:var(--ink);margin-top:3px}
  .sender-name{font-family:"Arimo",sans-serif;font-size:20px;color:var(--text);line-height:22px}
  .sender-line{font-family:"Arimo",sans-serif;font-size:11px;color:var(--text);line-height:14px}
  .notice{position:absolute;left:50px;top:150px;font-family:"Arimo",sans-serif;font-weight:700;font-size:16.5px;letter-spacing:.5px;color:var(--text)}
  .fill-line{position:absolute;left:50px;top:197px;font-family:"Arimo",sans-serif;font-weight:700;font-size:16.5px;color:var(--text);display:flex;align-items:flex-end}
  .blank{display:inline-block;border-bottom:1px solid var(--text);height:16px}
  .pitch{position:absolute;left:15px;top:263px;width:240px;font-family:"Arimo",sans-serif;font-weight:700;font-size:13px;line-height:16px;color:var(--text)}
  .to{position:absolute;left:280px;top:268px;font-family:"Arimo",sans-serif;font-weight:700;font-size:13px;color:var(--text)}
  .contact{position:absolute;left:15px;top:341px;font-family:"Arimo",sans-serif;font-weight:700;font-size:13px;line-height:17px;color:var(--text)}
</style>
</head>
<body>
<div class="sheet">

  <section class="front card-sold">
    <div class="photo map-inset" role="img" aria-label="Map of Florida with a circular inset of the community's coastline"></div>
    <div class="photo aerial" style="left:176px;top:14px;width:340px;height:121px" role="img" aria-label="Aerial view of the canal community and the gulf"></div>
    <div class="headline kicker" style="top:144px">Just Sold</div>
    <div class="headline place" style="top:170px">Amber Reed Landing</div>
    <div class="photo canal" style="left:12px;top:214px;width:506px;height:185px" role="img" aria-label="Boat cruising along a palm-lined canal with waterfront homes"></div>
    <div class="badge" style="left:333px;top:345px">
      <span class="badge-mark"></span>
      <div class="badge-text">harbor-lane realty<br>Nora Whitfield Broker</div>
    </div>
  </section>

  <section class="back card-sold">
    <div class="sender">
      <span class="sender-mark"></span>
      <div>
        <div class="sender-name">Nora Whitfield</div>
        <div class="sender-line">Harbor Lane Realty</div>
        <div class="sender-line">PO Box 418</div>
        <div class="sender-line">Cedar Point, FL 33900</div>
      </div>
    </div>
    <p class="notice">on your block of Amber Reed Landing has just sold</p>
    <p class="fill-line">at $&nbsp;&nbsp;<span class="blank" style="width:206px"></span>&nbsp;&nbsp;&nbsp;on&nbsp;&nbsp;<span class="blank" style="width:143px"></span></p>
    <p class="pitch">Please contact me if you are interested in buying or selling property in the area.</p>
    <p class="to">To:</p>
    <p class="contact">555-302-1187<br>norawhitfield@example.com</p>
  </section>

  <section class="front card-listed">
    <div class="photo map-inset" role="img" aria-label="Map of Florida with a circular inset of the community's coastline"></div>
    <div class="photo canal" style="left:181px;top:13px;width:338px;height:116px" role="img" aria-label="Boat cruising along a palm-lined canal with waterfront homes"></div>
    <div class="headline kicker" style="top:139px">Just Listed</div>
    <div class="headline place" style="top:165px">Amber Reed Landing</div>
    <div class="photo aerial" style="left:12px;top:214px;width:507px;height:182px" role="img" aria-label="Wide aerial view of the canal grid meeting the gulf"></div>
    <div class="badge" style="left:333px;top:343px">
      <span class="badge-mark"></span>
      <div class="badge-text">harbor-lane realty<br>Nora Whitfield Broker</div>
    </div>
  </section>

  <section class="back card-listed">
    <div class="sender">
      <span class="sender-mark"></span>
      <div>
        <div class="sender-name">Nora Whitfield</div>
        <div class="sender-line">Harbor Lane Realty</div>
        <div class="sender-line">PO Box 418</div>
        <div class="sender-line">Cedar Point, FL 33900</div>
      </div>
    </div>
    <p class="notice">on your block of Amber Reed Landing has just listed</p>
    <p class="fill-line">at $&nbsp;&nbsp;<span class="blank" style="width:206px"></span>&nbsp;&nbsp;&nbsp;on&nbsp;&nbsp;<span class="blank" style="width:143px"></span></p>
    <p class="pitch">Please contact me if you are interested in buying or selling property in the area.</p>
    <p class="to">To:</p>
    <p class="contact">555-302-1187<br>norawhitfield@example.com</p>
  </section>

</div>
</body>
</html>
```